Dance School Banner Design

Design a banner with landscape orientation for outdoor use and advertisement for Dance School.

Tha dance school is Marlow Street Dance Studio and they have their own logo (please message for the file to be sent to you) utilising lots of colour.

Their brand and uniform colours are purple and golden yellow.

Must have the name/logo.

Must attract all ages, boys and girls.

MSDS offers dance class for all ages and all levels of ability in the following dance styles:

Classical Ballet
Jazz
Tap
Modern / Contemporary
Hip Hop
Cheerleading
Vimbo (licensed logo is available please message for this)
Vimbokinetic (licensed logo is available please message for this)
Boys Class
Adults Classes

They offer all classes for fun or for competition.

Offer exams in Classical Ballet, Jazz and Tap.

Target Market(s)

All ages

Industry/Entity Type

Landscape

Requirements
Must have
• What classes are offered

Logo - 2 designs uploaded must use Marlow Street Dance Studio one, may wish to include home of "KESTRELS" logo aswell please message for this to be sent to you

Phone Number 0455 316 904

Email address marlow-steps@mailbreeze.net

website address marlowstreetsteps.com (this website is not live yet please see preview by using this link http://preview.dev.qelbrix.com/index.php?admin_action=preview_mod&site_id=5820471396&template_id=739&industry=qelbrixsites.com)
Nice to have
• Images of dancers (can provide some if needed)
Should not have
• Anything vulgar or discriminatory

```html
<!DOCTYPE html>
<html lang="en">
<head>
<meta charset="utf-8">
<title>Marlow Street Dance Studio Banner</title>
<link rel="stylesheet" href="https://fonts.googleapis.com/css2?family=Arimo:ital,wght@0,400;0,700;1,400&family=Comfortaa:wght@700&display=swap">
<style>
  :root {
    --stage-dark: #1c1c4e;
    --stage-mid: #34347e;
    --curtain-deep: #1f1f9a;
    --curtain-light: #5a5af0;
    --floor: #3434d6;
    --floor-light: #5050f2;
    --gold: #f4f41c;
    --white: #ffffff;
    --star: #27c6d8;
    --lime: #8cf51a;
    --orange: #f57a12;
    --blue: #2a5ef0;
    --violet: #b432e6;
    --aqua: #2fc6c6;
    --red: #e8283c;
    --vimbo-green: #b6e81e;
    --kestrel-gold: #f2c21c;
  }
  * { margin: 0; padding: 0; box-sizing: border-box; }
  html, body { width: 1200px; height: 624px; overflow: hidden; background: var(--stage-dark); }
  .banner {
    position: relative; width: 1200px; height: 624px; overflow: hidden;
    background: radial-gradient(ellipse at 50% 45%, var(--stage-mid) 0%, #272768 45%, var(--stage-dark) 100%);
    font-family: "Arimo", Arial, sans-serif; color: var(--white);
  }
  .art { position: absolute; }
  .valance { left: 0; top: 0; width: 1200px; height: 125px;
    background: linear-gradient(180deg, var(--curtain-deep) 0%, var(--curtain-light) 60%, #2a2aa8 100%);
    border-radius: 0 0 50% 50% / 0 0 30% 30%; }
  .curtain-left { left: 0; top: 0; width: 150px; height: 580px;
    background: linear-gradient(90deg, var(--curtain-deep), var(--curtain-light) 40%, var(--curtain-deep) 70%, #3b3bd0); }
  .curtain-right { right: 0; top: 0; width: 160px; height: 580px;
    background: linear-gradient(90deg, #3b3bd0, var(--curtain-deep) 30%, var(--curtain-light) 60%, var(--curtain-deep)); }
  .stage-floor { left: 0; top: 540px; width: 1200px; height: 84px;
    background: linear-gradient(180deg, var(--floor-light), var(--floor) 50%, #2020a8);
    border-radius: 50% 50% 0 0 / 35% 35% 0 0; }
  .dancer { border-radius: 45% 45% 40% 40%; opacity: .85; }
  .dancer-lime { left: 145px; top: 140px; width: 90px; height: 190px; background: radial-gradient(ellipse, var(--lime), transparent 72%); }
  .dancer-orange { left: 205px; top: 140px; width: 110px; height: 190px; background: radial-gradient(ellipse, var(--orange), transparent 72%); }
  .dancer-blue { left: 810px; top: 155px; width: 120px; height: 185px; background: radial-gradient(ellipse, var(--blue), transparent 72%); }
  .dancer-violet { left: 925px; top: 150px; width: 120px; height: 195px; background: radial-gradient(ellipse, var(--violet), transparent 72%); }
  .dancer-aqua { left: 305px; top: 390px; width: 190px; height: 210px; background: radial-gradient(ellipse, var(--aqua), transparent 72%); }
  .dancer-lowblue { left: 725px; top: 420px; width: 90px; height: 175px; background: radial-gradient(ellipse, var(--blue), transparent 72%); }

  .studio-name { position: absolute; left: 310px; top: 160px; width: 560px; text-align: center;
    font-family: "Comfortaa", "Trebuchet MS", sans-serif; font-weight: 700; color: var(--white); line-height: 1.05; }
  .studio-name .name-main { display: block; font-size: 66px; }
  .studio-name .name-sub { display: block; font-size: 40px; text-align: right; padding-right: 20px; margin-top: 10px; }

  .intro { position: absolute; left: 0; top: 354px; width: 1200px; text-align: center; font-size: 17.5px; font-weight: 700; }
  .classes { position: absolute; left: 140px; top: 385px; width: 920px; text-align: center;
    color: var(--gold); font-weight: 700; font-size: 18.5px; line-height: 26.5px; }
  .classes .star { display: inline-block; width: 14px; height: 14px; vertical-align: -1px; margin: 0 3px; }
  .classes .gap { display: inline-block; width: 16px; }

  .exams, .purpose { position: absolute; font-style: italic; font-size: 17px; line-height: 20px; }
  .exams { left: 166px; top: 478px; }
  .purpose { left: 780px; top: 492px; width: 240px; text-align: center; }

  .phone { position: absolute; left: 0; top: 518px; width: 1200px; text-align: center; padding-left: 10px;
    color: var(--gold); font-weight: 700; font-size: 52px; letter-spacing: 1px; }
  .web, .email { position: absolute; top: 562px; font-style: italic; font-size: 23px; }
  .web { left: 38px; }
  .email { right: 22px; }

  .partner { position: absolute; font-weight: 700; }
  .partner-kinetic { left: 18px; top: 427px; font-size: 19px; color: var(--red); }
  .partner-vimbo { left: 1080px; top: 342px; text-align: center; font-size: 18px; color: var(--white); }
  .partner-vimbo .dot { display: block; width: 22px; height: 22px; margin: 0 auto 6px; border-radius: 50%; background: var(--vimbo-green); }
  .partner-kestrels { left: 1030px; top: 445px; width: 140px; text-align: center; font-size: 24px; color: var(--kestrel-gold); }
  .partner-kestrels .mark { display: block; width: 40px; height: 40px; margin: 8px auto 0; background: var(--kestrel-gold); }
</style>
</head>
<body>
<main class="banner">
  <div class="art valance" role="img" aria-label="Draped purple stage curtain valance"></div>
  <div class="art curtain-left" role="img" aria-label="Purple stage curtain on the left"></div>
  <div class="art curtain-right" role="img" aria-label="Purple stage curtain on the right"></div>
  <div class="art stage-floor" role="img" aria-label="Blue stage floor"></div>

  <div class="art dancer dancer-lime" role="img" aria-label="Lime green dancer silhouette"></div>
  <div class="art dancer dancer-orange" role="img" aria-label="Orange dancer silhouette leaping"></div>
  <div class="art dancer dancer-blue" role="img" aria-label="Blue ballet dancer silhouette"></div>
  <div class="art dancer dancer-violet" role="img" aria-label="Purple ballerina silhouette"></div>
  <div class="art dancer dancer-aqua" role="img" aria-label="Aqua dancer silhouette in an arabesque"></div>
  <div class="art dancer dancer-lowblue" role="img" aria-label="Blue dancer silhouette"></div>

  <h1 class="studio-name"><span class="name-main">Marlow Street</span><span class="name-sub">dance studio</span></h1>

  <p class="intro">MSDS offers dance class for all ages and all levels of ability in the following dance styles:</p>

  <p class="classes">
    Classical Ballet<svg class="star" viewBox="0 0 20 20"><polygon fill="var(--star)" points="10,1 12.6,7.2 19.5,7.6 14.2,12 15.9,18.8 10,15 4.1,18.8 5.8,12 0.5,7.6 7.4,7.2"/></svg>Jazz<span class="gap"></span>Tap<svg class="star" viewBox="0 0 20 20"><polygon fill="var(--star)" points="10,1 12.6,7.2 19.5,7.6 14.2,12 15.9,18.8 10,15 4.1,18.8 5.8,12 0.5,7.6 7.4,7.2"/></svg>Modern / Contemporary<svg class="star" viewBox="0 0 20 20"><polygon fill="var(--star)" points="10,1 12.6,7.2 19.5,7.6 14.2,12 15.9,18.8 10,15 4.1,18.8 5.8,12 0.5,7.6 7.4,7.2"/></svg>Hip Hop<span class="gap"></span>Cheerleading<br>
    Vimbo<svg class="star" viewBox="0 0 20 20"><polygon fill="var(--star)" points="10,1 12.6,7.2 19.5,7.6 14.2,12 15.9,18.8 10,15 4.1,18.8 5.8,12 0.5,7.6 7.4,7.2"/></svg>Vimbokinetic<span class="gap"></span>Boys Classes<svg class="star" viewBox="0 0 20 20"><polygon fill="var(--star)" points="10,1 12.6,7.2 19.5,7.6 14.2,12 15.9,18.8 10,15 4.1,18.8 5.8,12 0.5,7.6 7.4,7.2"/></svg>Adults Classes<svg class="star" viewBox="0 0 20 20"><polygon fill="var(--star)" points="10,1 12.6,7.2 19.5,7.6 14.2,12 15.9,18.8 10,15 4.1,18.8 5.8,12 0.5,7.6 7.4,7.2"/></svg>Stunt and Tumbling<br>
    Strength/Conditioning
  </p>

  <p class="exams">Offer exams in<br>Classical Ballet,<br>Jazz and Tap.</p>
  <p class="purpose">They offer all classes for<br>fun or for competition.</p>

  <p class="phone">0455 316 904</p>
  <p class="web">www.marlowstreetsteps.com</p>
  <p class="email">marlow-steps@mailbreeze.net</p>

  <p class="partner partner-kinetic">Vimbokinetic</p>
  <p class="partner partner-vimbo"><span class="dot"></span>Vimbo</p>
  <p class="partner partner-kestrels">KESTRELS<span class="mark"></span></p>
</main>
</body>
</html>
```